Etiketten-Design für Imkerei
Zielgruppe
Wir sind eine kleine Imkerei die sich vorwiegend auf Honig konzentriert. Waldhonig und Wald-Blütenhonig .
Zielgruppe sind alle die gerne Qualitätshonig aus der Region kaufen .
Aufgabenstellung
es sind 2 verschiedene Etiketten Größen für verschieden Nettofüllmengen :
250 g - H 3,5 cm ,B 12 cm
500 g - H 5 cm , B 17 cm
Honigsortenbezeichnung je einmal 'Wald' einmal 'Wald-Blüten' sollte aber möglich sein auch andere Honigsorten anzugeben.
die gesetzlichen Vorschriften der Schriftgröße für Adresse, Haltbarkeit und 100% Honig aus Österreich sind 1,2 mm immer vom kleinsten Buchstaben ausgehend . Ausgenommen NETTOFÜLLMENGE muss mind. 4 mm sein auch vom kleinsten Buchstaben ausgehend .
die Adresse und Mindestens Haltbar bis auf der linken Seite der Etikette( muss auf der gleichen Seite stehen) , in der Mitte Schriftzug mit Grafik wobei hier die Größe keiner Vorschrift unterliegt.
Sortenbezeichnung kann in der Mitte sein muss aber nicht und rechts neben Schriftzug „KOLMER`S HONIG“ die Nettofüllmenge , ganz rechts dann 100% Honig aus Österreich
Die Hintergrundfarbe der Etiketten sollten in Granitgrau- Schwarz lebendig also ähnlich wie marmoriert sein.
Schriftzug in der Mitte : ' Kolmer`s Honig ' das 'B' sollte eine Biene sein , den Rest überlasse ich Euch Profis . Schriftfarbe nicht Metallic oder Gold da die Deckel Silber sind. Fotos füge ich unten ein wobei es weder diese Biene sein muss noch der Schriftzug das ist nur ein Beispiel. Das ganze sollte edel und doch verspielt aussehen . Den Schriftzug Kolmer`s Honig möchte ich in weiterer Folge auch alleine verwenden können wie zB. für Rechnungen oder Homepage .
Angaben auf der Etikette wie oben beschrieben:
Imkerei
T & L Wimmerhuber
Tannenhoferweg 214
9563 Lindenau
+436608274316 1,2 mm ausgehend vom kleinsten Buchstaben
Mindestens Haltbar bis:
siehe Glasunterseite
Trocken und vor Wärme geschützt Lagern ! 1,2 mm ausgehend vom kleinsten Buchstaben

```html
<!DOCTYPE html>
<html lang="de">
<head>
<meta charset="utf-8">
<title>Kolmer`s Honig – Etikette Wald-Blüten-Honig 500 g</title>
<link rel="stylesheet" href="https://fonts.googleapis.com/css2?family=Cinzel:wght@400;500&family=Encode+Sans+Condensed:wght@400&family=Open+Sans:wght@400&display=swap">
<style>
  :root {
    --page: #ffffff;
    --label-deep: #0e0e0d;
    --label-mid: #1d1d1b;
    --label-light: #2a2927;
    --honey-green: #8c9b16;
    --warm-taupe: #a39a86;
    --muted-text: #9a927f;
    --ring-tone: #4f4a3f;
  }
  * { box-sizing: border-box; margin: 0; padding: 0; }
  html, body {
    width: 1200px;
    height: 848px;
    overflow: hidden;
    background: var(--page);
  }
  .canvas {
    position: relative;
    width: 1200px;
    height: 848px;
  }
  .label {
    position: absolute;
    left: 18px;
    top: 252px;
    width: 1164px;
    height: 343px;
    overflow: hidden;
    background:
      radial-gradient(ellipse 40% 60% at 75% 45%, var(--label-light) 0%, transparent 70%),
      radial-gradient(ellipse 35% 55% at 20% 30%, var(--label-mid) 0%, transparent 75%),
      linear-gradient(180deg, var(--label-mid) 0%, var(--label-deep) 100%);
  }
  .floral-band {
    position: absolute;
    left: 0;
    bottom: 0;
    width: 100%;
    height: 180px;
    background:
      radial-gradient(ellipse 24% 75% at 12% 100%, rgba(74,69,58,0.55), transparent 75%),
      radial-gradient(ellipse 26% 85% at 88% 100%, rgba(74,69,58,0.55), transparent 75%),
      radial-gradient(ellipse 30% 55% at 50% 100%, rgba(74,69,58,0.35), transparent 75%);
  }
  .brand-ring {
    position: absolute;
    left: 450px;
    top: 82px;
    width: 256px;
    height: 256px;
  }
  .info-left {
    position: absolute;
    left: 29px;
    top: 27px;
    font-family: "Encode Sans Condensed", "Arial Narrow", sans-serif;
    font-size: 18px;
    line-height: 24px;
    color: var(--muted-text);
  }
  .info-left p + p { margin-top: 10px; }
  .brand-name {
    position: absolute;
    left: 0;
    width: 100%;
    top: 50px;
    display: flex;
    justify-content: center;
    align-items: center;
    gap: 12px;
    font-family: "Cinzel", serif;
    font-weight: 400;
    font-size: 36px;
    color: var(--warm-taupe);
  }
  .brand-dot {
    width: 18px;
    height: 18px;
    border-radius: 50%;
    background: var(--honey-green);
  }
  .variety {
    position: absolute;
    left: 0;
    width: 100%;
    top: 178px;
    text-align: center;
    font-family: "Cinzel", serif;
    font-weight: 500;
    font-size: 40px;
    line-height: 44px;
    letter-spacing: 1px;
    color: var(--honey-green);
  }
  .origin {
    position: absolute;
    right: 17px;
    top: 13px;
    font-family: "Open Sans", sans-serif;
    font-size: 20px;
    color: var(--honey-green);
  }
  .net-weight {
    position: absolute;
    left: 1037px;
    top: 55px;
    font-family: "Open Sans", sans-serif;
    font-size: 22px;
    line-height: 33px;
    color: var(--muted-text);
  }
</style>
</head>
<body>
  <main class="canvas">
    <section class="label">
      <div class="floral-band" role="img" aria-label="Gravierte Blüten- und Blattranken als Ornamentband am unteren Rand"></div>

      <svg class="brand-ring" viewBox="0 0 256 256" aria-hidden="true">
        <path d="M 200 38 A 124 124 0 1 1 30 58" fill="none" stroke="var(--ring-tone)" stroke-width="4" stroke-linecap="round"/>
      </svg>

      <div class="info-left">
        <p>Imkerei<br>T &amp; L Wimmerhuber<br>Tannenhoferweg 214<br>9563 Lindenau</p>
        <p>Mindestens Haltbar bis:<br>siehe Glasunterseite</p>
        <p>Trocken und vor Wärme geschützt<br>Lagern !</p>
      </div>

      <div class="brand-name">
        <span class="brand-dot"></span>
        <span>Kolmer`s Honig</span>
      </div>

      <h1 class="variety">Wald-Blüten-<br>Honig</h1>

      <p class="origin">Honig aus Österreich</p>
      <p class="net-weight">Füllmenge<br>500g</p>
    </section>
  </main>
</body>
</html>
```